Illustration Design for all Advertising & Event Material

To create an illustrative style that represents our brand and key messages to clients which shows the company’s personality and character, without depicting people specifically.

The key message should be expressed in a way that asks the viewer to engage and decode the image for themselves. We are looking for intelligent, sophisticated, premium design rather obvious, playful and quirky.

The illustrative concept will be used across our collateral including: Advertising – print and digital, client presentations, stands at European trade events and client brochures.

About us:
We are global consultancy who advises investors looking at hotels. Our team is uniquely positioned as a comprehensive, international service provider focused exclusively on hospitality.

Message to illustrate:
“Thinking differently has always been a part of our company’s DNA and we pride ourselves on it — we’re constantly challenging the status quo and resolving complex challenges with innovative solutions”

Target Market(s)

B2B Hotel / Hospitality Investment Market

Industry/Entity Type

Investment

Font styles to use
Sans Serif
Other font styles liked:
• Headers San-Serif / Body copy Serif

Requirements
Must have
• Correct colour palette - please see uploaded Colour Palette PDF
Nice to have
• Please also see uploaded Style & Characteristics PDF for styling "likes"

```html
<!DOCTYPE html>
<html lang="en">
<head>
<meta charset="utf-8">
<title>Thinking Differently – Brochure Cover</title>
<link rel="stylesheet" href="https://fonts.googleapis.com/css2?family=Didact+Gothic&display=swap">
<style>
  :root {
    --backdrop: #e4e9e8;
    --paper: #ffffff;
    --photo-light: #efcfa6;
    --photo-dark: #a2603a;
    --charcoal: #2a2e2f;
    --lime: #72ff05;
    --forest: #034a19;
    --chartreuse: #b4f52f;
    --bright-green: #08e51f;
    --brand-green: #009029;
    --icon-lime: #6fe816;
    --icon-green: #0a7a2b;
    --text-green: #0c9a34;
  }
  html, body {
    margin: 0;
    padding: 0;
    width: 1200px;
    height: 1200px;
    overflow: hidden;
    background: var(--backdrop);
  }
  .cover {
    position: absolute;
    left: 146px;
    top: 0;
    width: 907px;
    height: 1200px;
    background: var(--paper);
    overflow: hidden;
  }
  .cover__art {
    position: absolute;
    inset: 0;
    width: 100%;
    height: 100%;
  }
  .cover__quote {
    position: absolute;
    left: 46px;
    top: 978px;
    margin: 0;
    font-family: "Didact Gothic", "Century Gothic", sans-serif;
    font-size: 22px;
    line-height: 23.5px;
    letter-spacing: -0.2px;
    word-spacing: -1px;
    color: var(--text-green);
    white-space: nowrap;
  }
</style>
</head>
<body>
  <main class="cover">
    <svg class="cover__art" viewBox="0 0 883 1168" preserveAspectRatio="none" xmlns="http://www.w3.org/2000/svg">
      <defs>
        <linearGradient id="photo-tone" x1="0" y1="0" x2="0" y2="1">
          <stop offset="0" stop-color="var(--photo-light)"/>
          <stop offset="1" stop-color="var(--photo-dark)"/>
        </linearGradient>
        <linearGradient id="panel-shade" x1="0" y1="0" x2="1" y2="0">
          <stop offset="0" stop-color="#000" stop-opacity="0.12"/>
          <stop offset="1" stop-color="#000" stop-opacity="0"/>
        </linearGradient>
      </defs>

      <polygon class="cover__photo" role="img" aria-label="Photograph area: city high-rise towers against a warm sunrise sky"
               points="0,0 883,0 883,498 473,706 0,475" fill="url(#photo-tone)"/>

      <g class="cover__facets">
        <polygon class="facet facet--charcoal" points="0,473 240,588 0,702" fill="var(--charcoal)"/>
        <polygon class="facet facet--lime" points="0,702 240,586 240,818" fill="var(--lime)"/>
        <polygon class="facet facet--forest" points="240,586 473,706 240,818" fill="var(--forest)"/>
        <polygon class="facet facet--chartreuse" points="243,818 473,706 473,933" fill="var(--chartreuse)"/>
        <polygon class="facet facet--bright" points="473,706 705,820 473,933" fill="var(--bright-green)"/>
        <polygon class="facet-shadow" points="700,822 883,906 883,930 705,830" fill="url(#panel-shade)"/>
        <polygon class="facet facet--brand" points="473,706 883,498 883,906" fill="var(--brand-green)"/>
      </g>

      <g class="cover__marker">
        <polygon points="21,910 70,935 21,935" fill="var(--brand-green)"/>
        <polygon points="21,935 70,935 21,961" fill="var(--chartreuse)"/>
      </g>

      <g class="cover__icons" fill="#fff">
        <g class="icon icon--profile">
          <circle cx="570" cy="1081" r="24" fill="var(--icon-lime)"/>
          <circle cx="570" cy="1076" r="4"/>
          <path d="M562 1087 q0 -7 8 -7 q8 0 8 7 z"/>
        </g>
        <g class="icon icon--search">
          <circle cx="682" cy="1081" r="24" fill="var(--icon-green)"/>
          <circle cx="684" cy="1079" r="4.5" fill="none" stroke="#fff" stroke-width="2"/>
          <line x1="680.5" y1="1082.5" x2="676" y2="1087" stroke="#fff" stroke-width="2.4" stroke-linecap="round"/>
        </g>
        <g class="icon icon--home">
          <circle cx="797" cy="1081" r="24" fill="var(--icon-green)"/>
          <path d="M789 1081 L797 1073 L805 1081 L803 1081 L803 1088 L799 1088 L799 1083 L795 1083 L795 1088 L791 1088 L791 1081 Z"/>
        </g>
      </g>
    </svg>

    <p class="cover__quote">“Thinking differently has always been a part of our compa-<br>ny’s DNA and we pride ourselves on it — we’re constantly<br>challenging the status quo and resolving complex chal-<br>lenges with innovative solutions”</p>
  </main>
</body>
</html>
```